Postcard Design

THE BRAMBLEWOOD AGENCY--MORTGAGE; FINAL EXPENSE; COLLEGE FUNDS; FINANCIAL PLANNING; FEATURING DISABILITY INCOME RIDERS; ACCIDENTAL DEATH RIDERS; CHILDREN&GRANDCHILDREN RIDERS; LIVING DEATH BENEFIT RIDERS; WAIVE PREMIUM RIDERS; AND UNEMPLOYMENT RIDERS

IF INTERESTED AND WANT MORE DETAILS PLEASE CONTACT: MIRTA DOLLEN @ 555-417-2093

Industry/Entity Type

College

```html
<!DOCTYPE html>
<html lang="en">
<head>
<meta charset="utf-8">
<title>The Bramblewood Agency Postcard</title>
<link href="https://fonts.googleapis.com/css2?family=Oswald:wght@500;700&display=swap" rel="stylesheet">
<style>
  :root {
    --teal: #3daf94;
    --teal-light: #a0d8cb;
    --paper: #ffffff;
    --backdrop: #efefef;
  }
  * { margin: 0; padding: 0; box-sizing: border-box; }
  html, body { width: 1200px; height: 961px; overflow: hidden; }
  body {
    background: var(--backdrop);
    position: relative;
    font-family: "Oswald", "Arial Narrow", sans-serif;
  }
  .postcard-front {
    position: absolute;
    left: 390px; top: 126px;
    width: 425px; height: 327px;
    background: var(--paper);
  }
  .brand-band {
    position: absolute;
    left: 21px; top: 1px;
    width: 160px; height: 99px;
    background: var(--teal);
    color: var(--paper);
    text-align: center;
    font-weight: 700;
    text-transform: uppercase;
    line-height: 1;
    padding-top: 15px;
  }
  .brand-band .brand-top { display: block; font-size: 20px; letter-spacing: 0.2px; }
  .brand-band .brand-main { display: block; font-size: 22px; margin-top: 6px; letter-spacing: 0.2px; }
  .services {
    position: absolute;
    left: 10px; top: 140px;
    width: 182px;
    color: var(--teal);
    font-weight: 500;
    font-size: 8.6px;
    line-height: 12.9px;
    text-align: center;
    text-transform: uppercase;
    list-style: none;
  }
  .contact-bar {
    position: absolute;
    left: 21px; top: 242px;
    width: 160px; height: 25px;
    background: var(--teal);
    color: var(--paper);
    font-weight: 500;
    font-size: 6.8px;
    line-height: 9.5px;
    text-align: center;
    padding-top: 3px;
    text-transform: uppercase;
  }
  .postage-area {
    position: absolute;
    left: 323px; top: 13px;
    width: 93px; height: 89px;
    border: 3px solid var(--teal);
    color: var(--teal);
    font-weight: 500;
    font-size: 9px;
    line-height: 13px;
    text-align: center;
    text-transform: uppercase;
    display: flex; align-items: center; justify-content: center;
  }
  .address-line {
    position: absolute;
    left: 247px;
    width: 143px;
    height: 2px;
    background: var(--teal);
  }
  .postcard-back {
    position: absolute;
    left: 386px; top: 506px;
    width: 425px; height: 328px;
    background: radial-gradient(circle at 40% 45%, var(--teal-light) 0%, #6cc3ae 55%, var(--teal) 100%);
  }
</style>
</head>
<body>
  <section class="postcard-front">
    <div class="brand-band">
      <span class="brand-top">The Bramblewood</span>
      <span class="brand-main">Agency</span>
    </div>
    <ul class="services">
      <li>Mortgage Final Expense,</li>
      <li>College Funds, Financial Planning,</li>
      <li>Featuring Disability Income Riders,</li>
      <li>Accidental Death Riders,</li>
      <li>Children-Grandchildren Riders,</li>
      <li>Living Death Benefit Riders,</li>
      <li>Waive Premium Riders,</li>
      <li>&amp; Unemployment Riders</li>
    </ul>
    <div class="contact-bar">
      If interested and want more details<br>
      Please contact: Mirta Dollen 555-417-2093
    </div>
    <div class="postage-area">Postage<br>Area</div>
    <div class="address-line" style="top:189px"></div>
    <div class="address-line" style="top:214px"></div>
    <div class="address-line" style="top:239px"></div>
    <div class="address-line" style="top:265px"></div>
  </section>
  <section class="postcard-back" role="img" aria-label="Decorative pattern of light mint pinwheel flowers on a teal background"></section>
</body>
</html>
```